Business Card Design Project

I need a business card designed from scratch. I have an existing logo that I can upload in Illustrator for modification or redesign.

The Company is called Rank Harbor http://rankharbor.com.au and we provide Search Engine Optimization services to Australian businesses. The current logo signifies an increase in visitors, profits etc...

There are no restrictions as to the redesign - colours, style etc are all open to change.

Cards will be full colour and one sided printed at http://www.printlorvex.com.au so check their requirements for file format and sizes etc.

I will expect all original files upon completion of project.

Target Market(s)

Any business with a web site looking to improve their search engine rankings

Industry/Entity Type

Business

Requirements
Must have
• I like modern, sleek designs. Clean, not fussy, uncluttered.

```html
<!DOCTYPE html>
<html lang="en">
<head>
<meta charset="utf-8">
<title>Rank Harbor – Business Card</title>
<link href="https://fonts.googleapis.com/css2?family=Arimo:wght@400;700&display=swap" rel="stylesheet">
<style>
  :root {
    --brand-blue: #1e78c2;
    --brand-navy: #173d70;
    --brand-yellow: #f7b924;
    --text-grey: #3f3f3f;
    --card-white: #ffffff;
    --page-bg: #ffffff;
  }
  * { margin: 0; padding: 0; box-sizing: border-box; }
  html, body {
    width: 1200px;
    height: 901px;
    overflow: hidden;
    background: var(--page-bg);
    font-family: "Arimo", Arial, sans-serif;
  }
  .card {
    position: absolute;
    left: 107px;
    top: 165px;
    width: 982px;
    height: 546px;
    background: var(--card-white);
    outline: 1px solid #ececec;
    overflow: hidden;
  }
  .brand {
    position: absolute;
    left: 62px;
    top: 86px;
    display: flex;
    align-items: center;
    gap: 18px;
  }
  .brand-dot {
    width: 34px;
    height: 34px;
    border-radius: 50%;
    background: var(--brand-yellow);
  }
  .brand-name {
    font-size: 66px;
    font-weight: 700;
    color: var(--brand-blue);
    letter-spacing: -1px;
    line-height: 1;
  }
  .edge-marker {
    position: absolute;
    left: 0;
    top: 331px;
    width: 32px;
    height: 62px;
  }
  .person {
    position: absolute;
    left: 72px;
    top: 328px;
    color: var(--text-grey);
  }
  .person-name {
    font-size: 32px;
    font-weight: 700;
    color: var(--brand-blue);
    line-height: 1.1;
  }
  .person-title {
    font-size: 24px;
    margin-top: 6px;
  }
  .address {
    margin-top: 32px;
    font-size: 25px;
    line-height: 33px;
    font-style: normal;
  }
  .contact-list {
    position: absolute;
    right: 38px;
    top: 332px;
    list-style: none;
    font-size: 25px;
    line-height: 32px;
    color: var(--text-grey);
    text-align: right;
  }
  .contact-list li {
    display: flex;
    justify-content: flex-end;
    align-items: center;
    gap: 14px;
  }
  .contact-icon {
    width: 20px;
    height: 20px;
    flex: none;
  }
  .footer-band {
    position: absolute;
    left: 0;
    bottom: 0;
    width: 100%;
    height: 32px;
    display: flex;
  }
  .footer-band .band-blue {
    width: 546px;
    background: linear-gradient(90deg, var(--brand-blue), var(--brand-navy));
  }
  .footer-band .band-yellow {
    flex: 1;
    background: var(--brand-yellow);
  }
</style>
</head>
<body>
  <main class="card">
    <div class="brand">
      <span class="brand-dot"></span>
      <span class="brand-name">Rank Harbor</span>
    </div>

    <svg class="edge-marker" viewBox="0 0 32 62" aria-hidden="true">
      <polygon points="0,0 32,31 0,62" fill="var(--brand-yellow)"/>
    </svg>

    <section class="person">
      <h1 class="person-name">Daniel Whitcombe</h1>
      <p class="person-title">Founder &amp; CEO</p>
      <address class="address">
        1180 Marlow Street #204<br>
        Dunmore, FL 32906
      </address>
    </section>

    <ul class="contact-list">
      <li>1300 555 018
        <svg class="contact-icon" viewBox="0 0 20 20" aria-label="phone"><path d="M5 2l3 4-2 2c1 2 3 4 5 5l2-2 4 3-2 3C9 17 3 11 2 5z" fill="var(--brand-blue)"/></svg>
      </li>
      <li>1300 555 018
        <svg class="contact-icon" viewBox="0 0 20 20" aria-label="mobile"><rect x="6" y="2" width="8" height="16" rx="1.5" fill="none" stroke="var(--brand-blue)" stroke-width="2"/><circle cx="10" cy="15" r="1" fill="var(--brand-blue)"/></svg>
      </li>
      <li>1300 555 018
        <svg class="contact-icon" viewBox="0 0 20 20" aria-label="fax"><rect x="5" y="2" width="10" height="5" fill="var(--brand-blue)"/><rect x="2" y="7" width="16" height="7" rx="1" fill="var(--brand-blue)"/><rect x="5" y="12" width="10" height="6" fill="#fff" stroke="var(--brand-blue)" stroke-width="1.5"/></svg>
      </li>
      <li>enquiry@rankharbor.com.au
        <svg class="contact-icon" viewBox="0 0 20 20" aria-label="email"><rect x="2" y="4" width="16" height="12" fill="var(--brand-blue)"/><path d="M2 4l8 7 8-7" fill="none" stroke="#fff" stroke-width="1.5"/></svg>
      </li>
      <li>www.rankharbor.com.au
        <svg class="contact-icon" viewBox="0 0 20 20" aria-label="website"><circle cx="10" cy="10" r="8" fill="var(--brand-blue)"/><path d="M2 10h16M10 2c-4 4-4 12 0 16M10 2c4 4 4 12 0 16" fill="none" stroke="#fff" stroke-width="1.2"/></svg>
      </li>
    </ul>

    <div class="footer-band">
      <div class="band-blue"></div>
      <div class="band-yellow"></div>
    </div>
  </main>
</body>
</html>
```